Real Estate - Property Management Business needs a Landlords Handbook designed

We need a landlord's handbook designed. We are a specialist property management business. The text and logos are there. The book needs images and to present more as a book. We would like to see designs that use orange, grey and white.
Our website is www.tallowbrook.com.au to give you an idea of our brand.

Target Market(s)

Professional couples - property investors

Industry/Entity Type

Real Estate

Font styles to use
Sans Serif

Colors
ffffff
1b1b1b
f37122

Requirements
Must have
• Images of property owners and applicable images
Nice to have
• The Pemberlys owner handbook is a guide to show you what I am looking for
Should not have
• This needs to look professional. No cartoon images

```html
<!DOCTYPE html>
<html lang="en">
<head>
<meta charset="utf-8">
<title>Tallowbrook Owner's Handbook</title>
<link href="https://fonts.googleapis.com/css2?family=Libre+Franklin:wght@400;500;700;800&display=swap" rel="stylesheet">
<style>
  :root {
    --orange: #f4530c;
    --orange-soft: #f37122;
    --ink: #1b1b1b;
    --white: #ffffff;
    --cover-grey: #cccccc;
    --footer-grey: #d6dfe0;
  }
  * { margin: 0; padding: 0; box-sizing: border-box; }
  html, body { width: 1200px; height: 1200px; overflow: hidden; background: var(--white); }
  body { position: relative; font-family: "Libre Franklin", Arial, sans-serif; color: var(--ink); }

  .cover { position: absolute; left: 440px; top: 0; width: 316px; height: 444px; border: 1px solid #999; border-bottom: none; background: var(--white); }
  .cover__mark { position: absolute; left: 222px; top: 22px; width: 48px; height: 48px; background: var(--orange); }
  .cover__title { position: absolute; right: 9px; top: 162px; text-align: right; color: var(--orange); font-weight: 800; font-size: 38px; line-height: 34px; }
  .cover__band { position: absolute; left: 0; right: 0; top: 355px; height: 10px; background: var(--orange); }
  .cover__foot { position: absolute; left: 0; right: 0; top: 365px; bottom: 0; background: var(--cover-grey); }
  .cover__brand { position: absolute; right: 4px; bottom: 5px; font-size: 20px; font-weight: 700; color: var(--orange); }

  .spread { position: absolute; left: 96px; top: 482px; width: 1004px; height: 718px; border: 1px solid #333; border-bottom: none; background: var(--white); overflow: hidden; }
  .photo { position: absolute; box-shadow: 0 6px 10px rgba(0,0,0,.35); border: 7px solid #eee; }
  .photo--room { left: 71px; top: 59px; width: 366px; height: 247px; background: linear-gradient(180deg, #e8e9e6 0%, #d9dad6 55%, #c9c3b6 100%); }
  .welcome__title { position: absolute; left: 30px; top: 352px; font-size: 19px; font-weight: 700; color: var(--orange); }
  .welcome__body { position: absolute; left: 30px; top: 393px; font-size: 13px; line-height: 17px; letter-spacing: .1px; white-space: nowrap; }
  .welcome__body strong { color: var(--orange); }

  .team__title { position: absolute; left: 536px; top: 40px; font-size: 20px; font-weight: 700; color: var(--orange); }
  .member__photo { position: absolute; background: linear-gradient(180deg, #eeeeee 0%, #b9a38a 45%, #222 100%); }
  .member__photo--one { left: 519px; top: 71px; width: 95px; height: 141px; }
  .member__photo--two { left: 522px; top: 396px; width: 105px; height: 158px; }
  .member__name { position: absolute; font-size: 16px; font-weight: 700; color: var(--orange); white-space: nowrap; letter-spacing: -.1px; }
  .member__text { position: absolute; font-size: 12.6px; line-height: 16.9px; letter-spacing: -.2px; white-space: nowrap; }
  .name-one { left: 625px; top: 75px; }
  .text-one { left: 625px; top: 102px; }
  .text-one-wrap { left: 518px; top: 226px; }
  .name-two { left: 639px; top: 397px; }
  .text-two { left: 639px; top: 423px; }

  .spread__band { position: absolute; left: 0; right: 0; top: 566px; height: 28px; background: var(--orange); }
  .spread__foot { position: absolute; left: 0; right: 0; top: 594px; bottom: 0; background: var(--footer-grey); }
  .badge { position: absolute; top: 22px; height: 54px; }
  .badge--one { left: 30px; width: 80px; background: #d21f44; }
  .badge--two { left: 114px; width: 120px; background: var(--white); }
  .contact { position: absolute; left: 24px; top: 84px; font-size: 17px; font-weight: 700; }
  .spread__brand { position: absolute; right: 20px; top: 68px; font-size: 30px; font-weight: 700; color: var(--orange); }
</style>
</head>
<body>
  <section class="cover">
    <div class="cover__mark"></div>
    <h1 class="cover__title">Owner’s<br>handbook</h1>
    <div class="cover__band"></div>
    <div class="cover__foot"><div class="cover__brand">Tallowbrook</div></div>
  </section>

  <section class="spread">
    <div class="photo photo--room" role="img" aria-label="Bright empty living room with tiled floor and open kitchen"></div>
    <h2 class="welcome__title">Welcome to our agency.</h2>
    <p class="welcome__body"><strong>Tallowbrook</strong> is a dynamic and energetic specialist Property Man-<br>agement company, focused on providing the best service, advice and<br>support to you and your investment.<br>We continually invest in our team’s professional development and<br>learning, along with our systems, procedures and technology to ensure<br>that we are able to provide our clients with the highest level of service.</p>

    <h2 class="team__title">OUR TEAM</h2>
    <div class="member__photo member__photo--one" role="img" aria-label="Portrait of Claire Hadley"></div>
    <h3 class="member__name name-one">Claire Hadley – Principal Licensee</h3>
    <p class="member__text text-one">Claire is the Director of Property Management for<br>Tallowbrook and has over 13 years experience in the property<br>management industry. Committed to learning and extend-<br>ing her knowledge Claire has completed a Bachelor of<br>Business Majoring in Marketing, a Certificate IV in Property<br>Services (Real Estate) and is a licensed real estate agent.<br>Claire holds a reputation for consistently achieving excel-</p>
    <p class="member__text text-one-wrap">lent results within the dynamic areas of residential rental properties and<br>portfolio management. It is her professional approach and strong focus on<br>customer service that sets her apart. She is especially focused on building<br>strong relationships with owners and tenants alike, building trust through<br>clear and detailed communication, prompt follow-ups and a highly organised<br>approach to client management.<br>She enjoys the many challenges that she faces on a daily basis in her role<br>and thrives on being able to help clients with all aspects of real estate.<br>Claire is setting the bar when it comes to customer service in the property<br>management industry.</p>

    <div class="member__photo member__photo--two" role="img" aria-label="Portrait of Megan Astley"></div>
    <h3 class="member__name name-two">Megan Astley – Trust Account Administrator</h3>
    <p class="member__text text-two">Qualified and experienced property professional having<br>over 14 years experience in the real estate industry,<br>making trust account management her specialty. Megan<br>provides an unprecedented level of quality and profession-<br>alism. She feels privileged to be trusted with the responsi-<br>bility of assisting clients to achieve their financial goals.<br>Megan’s extensive experience as well as being an inves-<br>tor herself enables her to service all clients to a higher</p>

    <div class="spread__band"></div>
    <div class="spread__foot">
      <div class="badge badge--one"></div>
      <div class="badge badge--two"></div>
      <div class="contact">+61 7 3000 1234 | www.tallowbrook.com.au</div>
      <div class="spread__brand">Tallowbrook</div>
    </div>
  </section>
</body>
</html>
```